Vantrel Web Services

This is a new It services company operating in Perth western Australia

we need a website that is easy to navigate without a cluttered feel to it it should have the following links and pages

About Us
Services
Clients
Contact Us
MY Vantrel (login for clients)

Hi it is a web based IT services company so we would expect customers to come to the website for 2 different purposes the first is to enquire about our services and then as they become customers come to our website to manage their services so whilst they are seperate we want do not want it to look like 2 different websites

hope this helps

Hi to update this we need a home page and templates for sub pages

this is a design brief only and not the coding of the pages or building of the site

```html
<!DOCTYPE html>
<html lang="en">
<head>
<meta charset="utf-8">
<title>Vantrel Web Services</title>
<link href="https://fonts.googleapis.com/css2?family=Open+Sans:wght@400;600;700&display=swap" rel="stylesheet">
<style>
:root{
  --navy:#0d1f4f;
  --blue:#1a3ea0;
  --btn-blue:#0f2f8a;
  --red:#d9555a;
  --hex-blue:#3b67a8;
  --panel:#ebebeb;
  --text:#222;
  --white:#fff;
  --link:#b9c8ee;
}
*{margin:0;padding:0;box-sizing:border-box}
html,body{width:1200px;height:1000px;overflow:hidden;background:var(--white)}
body{position:relative;font-family:"Open Sans",Arial,sans-serif;color:var(--text)}
.page{position:absolute;left:342px;top:0;width:516px;height:1000px;background:var(--panel)}
.abs{position:absolute}
.nowrap{white-space:nowrap}
/* header */
.site-header{left:0;top:0;width:516px;height:45px;background:linear-gradient(#fafafa,#e6e6e6)}
.brand{left:65px;top:11px;display:flex;align-items:center;gap:5px}
.brand-mark{width:22px;height:22px;border-radius:50%;background:var(--red)}
.brand-name{font-size:15px;font-weight:600;color:var(--btn-blue);letter-spacing:.3px}
.client-login{left:396px;top:0;width:55px;height:20px;background:var(--btn-blue);color:var(--white);font-size:5.6px;font-weight:700;display:flex;align-items:center;justify-content:center;border-radius:0 0 3px 3px}
.main-nav a{position:absolute;top:25px;height:20px;font-size:5.8px;font-weight:600;color:var(--btn-blue);text-decoration:none;display:flex;align-items:center;justify-content:center}
.main-nav a.active{background:var(--navy);color:var(--white);border-radius:3px 3px 0 0}
/* hero */
.hero{left:0;top:45px;width:516px;height:166px;background:var(--navy)}
.hero-visual{left:65px;top:12px;width:191px;height:143px;background:linear-gradient(160deg,#c9d6e6,#5b7390 70%,#2a3a55);border-radius:4px}
.hero-arrow{top:65px}
.hero-title{left:279px;top:21px;color:var(--white);font-size:22px;font-weight:400;letter-spacing:.5px;line-height:28px}
.hero-sub{left:279px;top:51px;color:var(--white);font-size:15px;letter-spacing:3px;line-height:20px}
.hero-copy{left:279px;top:76px;color:var(--white);font-size:7.6px;line-height:12.5px;white-space:nowrap}
.pill{border-radius:11px;font-size:5.8px;font-weight:600;display:flex;align-items:center}
.quote-btn{left:279px;top:123px;width:82px;height:20px;background:linear-gradient(#f4f4f4,#cfcfcf);color:#333;justify-content:center}
/* sections */
.section-title{left:0;width:516px;text-align:center;color:var(--blue);font-size:15.5px;font-weight:400;letter-spacing:.4px;line-height:22px}
.title-rule{left:150px;width:216px;height:1px;background:linear-gradient(90deg,transparent,#c5c5c5,transparent)}
.intro{left:58px;top:262px;width:400px;text-align:center;font-size:5.3px;line-height:8.4px}
.service{top:290px;width:120px;text-align:center}
.service .hex{display:block;margin:0 auto}
.service h3{margin-top:11px;font-size:6px;font-weight:600;color:var(--blue)}
.service p{margin:4px auto 0;width:96px;font-size:5.2px;line-height:8.4px}
.details-btn{position:absolute;top:182px;left:23px;width:74px;height:21px;background:var(--btn-blue);color:var(--white);border-radius:11px;font-size:5.8px;font-weight:600;display:flex;align-items:center;padding-left:9px}
.details-btn svg,.visit-btn svg{position:absolute;right:9px}
.col-rule{top:300px;width:1px;height:90px;background:linear-gradient(transparent,#cfcfcf,transparent)}
/* showcase */
.showcase{left:0;top:505px;width:516px;height:161px;background:var(--navy)}
.showcase .section-title{color:var(--white);top:16px;letter-spacing:1.2px}
.project-name{left:65px;top:51px;color:var(--white);font-size:12px;font-weight:400;letter-spacing:.6px;line-height:18px}
.project-copy{left:65px;top:71px;width:258px;color:var(--white);font-size:5.2px;line-height:8.2px}
.visit-btn{left:65px;top:129px;width:74px;height:20px;background:linear-gradient(#f4f4f4,#cfcfcf);color:#333;padding-left:9px}
.project-shot{left:328px;top:56px;width:123px;height:92px;border:2px solid var(--white);background:linear-gradient(135deg,#0f6a96,#1ba3c9 55%,#0b3b66)}
.dots{display:flex;gap:4px}
.dots span{width:3px;height:3px;border-radius:50%;background:var(--white)}
.dots span.on{background:var(--red)}
/* seo */
.feature-icon{left:67px;width:24px;height:24px}
.feature h3{position:absolute;left:104px;font-size:8.5px;font-weight:400;color:#444;letter-spacing:.3px;line-height:12px}
.feature p{position:absolute;left:104px;width:346px;font-size:5.3px;line-height:8.4px}
.avatar{left:66px;top:854px;width:25px;height:25px;border-radius:50%;background:linear-gradient(#d8d8d8,#3b3b3b)}
.quote-mark{left:103px;top:850px;font-size:30px;color:#bdbdbd;font-family:Georgia,serif;line-height:30px}
.testimonial{left:124px;top:854px;font-size:5.2px;line-height:13px;color:#444;white-space:nowrap}
.testimonial cite{font-style:normal;color:var(--blue)}
.dots.grey span{border:1px solid #666;background:transparent;width:4px;height:4px}
.dots.grey span.on{background:#666}
/* footer */
.site-footer{left:0;top:900px;width:516px;height:100px;background:var(--navy);color:var(--white)}
.site-footer h4{position:absolute;top:10px;font-size:6.2px;font-weight:600}
.footer-about{left:66px;top:23px;width:124px;font-size:5.2px;line-height:8.2px;color:var(--link)}
.blog-list{left:196px;top:23px;list-style:none;font-size:5.4px;color:var(--link)}
.blog-list li{height:12.3px}
.blog-list li::before{content:"| ";color:#5d73b0}
.signup{left:327px;top:25px;width:115px;height:43px;background:#f2f2f2;border-radius:2px}
.field{position:absolute;left:7px;width:100px;height:13px;background:#dcdcdc;border-radius:2px;font-size:5px;color:#888;display:flex;align-items:center;padding-left:22px}
.signup-go{left:431px;top:36px;width:20px;height:20px;border-radius:50%;background:var(--white);display:flex;align-items:center;justify-content:center}
.footer-rule{left:0;top:77px;width:516px;height:1px;background:#1d3270}
.copyright{left:68px;top:90px;font-size:5.2px;color:var(--link)}
.social{top:90px;width:7px;height:7px;border:1px solid #8ea0d0;border-radius:50%}
</style>
</head>
<body>
<div class="page">

  <header class="abs site-header">
    <div class="abs brand"><span class="brand-mark"></span><span class="brand-name">Vantrel</span></div>
    <a class="abs client-login">MY VANTREL</a>
    <nav class="main-nav">
      <a class="active" style="left:277px;width:46px">ABOUT US</a>
      <a style="left:328px;width:35px">SERVICES</a>
      <a style="left:372px;width:30px">CLIENTS</a>
      <a style="left:412px;width:42px">CONTACT US</a>
    </nav>
  </header>

  <section class="abs hero">
    <div class="abs hero-visual" role="img" aria-label="Desktop monitor showing a web services site with a compass badge"></div>
    <svg class="abs hero-arrow" style="left:51px" width="10" height="17" viewBox="0 0 10 17"><path d="M8 1 2 8.5 8 16" fill="none" stroke="#fff" stroke-width="2.2"/></svg>
    <svg class="abs hero-arrow" style="left:455px" width="10" height="17" viewBox="0 0 10 17"><path d="M2 1 8 8.5 2 16" fill="none" stroke="#fff" stroke-width="2.2"/></svg>
    <h1 class="abs hero-title">24x7 ONLINE</h1>
    <div class="abs hero-sub">VANTREL</div>
    <p class="abs hero-copy">Phasellus a ipsum dapibus, viverra odio at,<br>pretium nisi. Phasellus euismod, eros a suscipit<br>euismod, at dapibus ligula erat sed elit.</p>
    <a class="abs pill quote-btn">GET A QUOTE FROM US</a>
  </section>

  <div class="abs title-rule" style="top:222px"></div>
  <h2 class="abs section-title" style="top:227px">WELCOME TO IT SERVICES</h2>
  <div class="abs title-rule" style="top:252px"></div>
  <p class="abs intro">Lorem ipsum dolor sit amet, consectetur adipiscing elit. Donec quis scelerisque quam. Fusce scelerisque massa eu nibh tristique, non tristique magna semper.<br>Nam et pharetra odio. Suspendisse facilisis libero sed metus vehicula feugiat. Aenean eu elit ut neque lobortis bibendum at et purus.</p>

  <div class="abs service" style="left:51px">
    <svg class="hex" width="92" height="108" viewBox="0 0 92 108"><polygon points="46,0 92,27 92,81 46,108 0,81 0,27" fill="var(--red)"/><rect x="22" y="30" width="48" height="48" rx="3" fill="#e9a06a" role="img" aria-label="Blueprint and ruler illustration"/></svg>
    <h3>PLANNING AND DESIGNING</h3>
    <p>Aliquam ornare facilisis accumsan. Suspendisse consequat, velit eu viverra biben dum, ligula mauris tristi que ante, sit amet tristiq eye ligula neque pelle lectus.</p>
    <a class="details-btn">VIEW DETAILS<svg width="7" height="6" viewBox="0 0 7 6"><path d="M0 2h4V0l3 3-3 3V4H0z" fill="#fff"/></svg></a>
  </div>
  <div class="abs col-rule" style="left:185px"></div>
  <div class="abs service" style="left:198px">
    <svg class="hex" width="92" height="108" viewBox="0 0 92 108"><polygon points="46,0 92,27 92,81 46,108 0,81 0,27" fill="var(--hex-blue)"/><rect x="27" y="28" width="38" height="52" rx="3" fill="#6f93c6" role="img" aria-label="Web markup standard emblem"/></svg>
    <h3>CODING &amp; CONVERSION</h3>
    <p>In dapibus elit ligula, et mollis tellus dictum et. Proin dapibus neque nec purus tempor pharetra in non tortor. Proin dapibus neque nec purus tempor in dapibus elit.</p>
    <a class="details-btn">VIEW DETAILS<svg width="7" height="6" viewBox="0 0 7 6"><path d="M0 2h4V0l3 3-3 3V4H0z" fill="#fff"/></svg></a>
  </div>
  <div class="abs col-rule" style="left:332px"></div>
  <div class="abs service" style="left:346px">
    <svg class="hex" width="92" height="108" viewBox="0 0 92 108"><polygon points="46,0 92,27 92,81 46,108 0,81 0,27" fill="var(--red)"/><circle cx="46" cy="54" r="24" fill="#e97b3a" role="img" aria-label="Web browser emblem"/></svg>
    <h3>TESTING &amp; MONITORING</h3>
    <p>Praesent venenatis sit amet neque et lobortis. Suspendisse euismod, purus ac cursus ultrices, dui dui dapibus neque, id molestie libero leo a nisl. Nunc ullamcorper eu.</p>
    <a class="details-btn">VIEW DETAILS<svg width="7" height="6" viewBox="0 0 7 6"><path d="M0 2h4V0l3 3-3 3V4H0z" fill="#fff"/></svg></a>
  </div>

  <section class="abs showcase">
    <h2 class="abs section-title">SEE OUR PROJECT SHOWCASE</h2>
    <h3 class="abs project-name">PHASELLUS A IPSUM</h3>
    <p class="abs project-copy">Ut blandit luctus turpis, vel pharetra ipsum volutpat et. Cras interdum ultricies ipsum, a posuere eros. Aenean nunc lacus, commodo at enim vel, aliquam tempor odio. Ut blandit luctus turpis, vel pharetra ipsum volutpat et. Cras interdum ultricies ipsum, a posuere eros. Aenean nunc lacus, commodo at enim vel, aliquam tempor odio. Vestibulum mollis, velit vitae varius dictum, sapien urna consectetur libero, eget sodales nunc massa sed dui. Aenean laoreet leo a sem vehicula condimentum. Curabitur posuere gravida ante sed vestibulum.</p>
    <a class="abs pill visit-btn">VISIT WEBSITE<svg width="7" height="6" viewBox="0 0 7 6"><path d="M0 2h4V0l3 3-3 3V4H0z" fill="#0d1f4f"/></svg></a>
    <div class="abs project-shot" role="img" aria-label="Business professional touching a digital world map interface"></div>
    <div class="abs dots" style="left:249px;top:151px"><span></span><span class="on"></span><span></span></div>
  </section>

  <div class="abs title-rule" style="top:676px"></div>
  <h2 class="abs section-title" style="top:682px">SEO AND PERFOMANCE TEST</h2>
  <div class="abs title-rule" style="top:707px"></div>

  <div class="feature">
    <svg class="abs feature-icon" style="top:728px" viewBox="0 0 24 24"><circle cx="12" cy="12" r="12" fill="var(--red)"/><path d="M9 8 5 12l4 4M15 8l4 4-4 4M13 7l-2 10" fill="none" stroke="#fff" stroke-width="1.3"/></svg>
    <h3 style="top:716px">PROIN FEUGIAT ALIQUET</h3>
    <p style="top:730px">Praesent venenatis sit amet neque et lobortis. Suspendisse euismod, purus ac cursus ultrices, dui dui dapibus neque. Sed ac tempor velit. Hasellus vehicula lorem in posuere porta. In aliquet lacus et semper semper. Donec pulvinar blandit tincidunt. posuere porta hasellus vehicula lorem in.</p>
  </div>
  <div class="abs" style="left:104px;top:762px;width:346px;height:1px;background:#d6d6d6"></div>
  <div class="feature">
    <svg class="abs feature-icon" style="top:778px" viewBox="0 0 24 24"><circle cx="12" cy="12" r="12" fill="var(--red)"/><path d="M8 6v12M12 6v12M16 6v12" stroke="#fff" stroke-width="1.3"/><rect x="6.5" y="9" width="3" height="3" fill="#fff"/><rect x="10.5" y="13" width="3" height="3" fill="#fff"/><rect x="14.5" y="8" width="3" height="3" fill="#fff"/></svg>
    <h3 style="top:767px">SED ELEIFEND TORTOR</h3>
    <p style="top:781px">Nulla eu nibh quis neque interdum tincidunt. Curabitur id lacus vel eros gravida accumsan. In congue eleifend diam eget vulputate. Am sed gravida libero. Aliquam at velit eu tortor tincidunt pharetra. Interdum et malesuada fames ac ante ipsum primis in faucibus. In aliquet lacus et semper semper.</p>
  </div>

  <div class="abs title-rule" style="top:816px"></div>
  <h2 class="abs section-title" style="top:821px">READ OUR TESTIMONIALS</h2>
  <div class="abs title-rule" style="top:846px"></div>
  <div class="abs avatar" role="img" aria-label="Client portrait"></div>
  <div class="abs quote-mark">&ldquo;</div>
  <p class="abs testimonial">Cras tempor tempus nulla, at venenatis dui suscipit at. In gravida lectus et mollis commodo. Cras ultrices ullamcorper mi vel porttitor.<br>Cras eros diam, tempus in consectetur tempus, ullamcorper nec velit" - <cite>Lorem Ipsum, 02.10.2014</cite></p>
  <div class="abs dots grey" style="left:249px;top:884px"><span></span><span class="on"></span><span></span></div>

  <footer class="abs site-footer">
    <h4 style="left:66px">ABOUT US</h4>
    <p class="abs footer-about">Curabitur varius, nisi nec euismod vehicula, tortor erat pulvinar mauris, vel tristique enim augue id orci. Sed nisl dolor, lacinia eget suscipit at, semper sed quam.</p>
    <h4 style="left:196px">LATEST ON BLOG</h4>
    <ul class="abs blog-list">
      <li>Phasellus mattis sodales urna at tincidunt</li>
      <li>Aenean laoreet leo a sem vehicula</li>
      <li>Donec quis scelerisque quam</li>
    </ul>
    <h4 style="left:327px">NEWSLETTER SIGNUP</h4>
    <div class="abs signup">
      <div class="field" style="top:7px">ENTER YOUR NAME</div>
      <div class="field" style="top:24px">ENTER YOUR EMAIL</div>
      <svg class="abs" style="left:12px;top:10px" width="7" height="7" viewBox="0 0 7 7"><circle cx="3.5" cy="2" r="1.8" fill="#666"/><path d="M0 7a3.5 3 0 0 1 7 0z" fill="#666"/></svg>
      <svg class="abs" style="left:12px;top:28px" width="7" height="5" viewBox="0 0 7 5"><rect width="7" height="5" fill="#666"/><path d="M0 0 3.5 3 7 0" fill="none" stroke="#dcdcdc" stroke-width=".7"/></svg>
    </div>
    <div class="abs signup-go"><svg width="13" height="13" viewBox="0 0 13 13"><circle cx="6.5" cy="6.5" r="6.5" fill="var(--navy)"/><path d="M3 5.6h4V3.5l3 3-3 3V7.4H3z" fill="#fff"/></svg></div>
    <div class="abs footer-rule"></div>
    <p class="abs copyright">&copy; Copyright 2014. All Rights Reserved . Vantrel</p>
    <span class="abs social" style="left:417px"></span>
    <span class="abs social" style="left:430px"></span>
    <span class="abs social" style="left:443px"></span>
  </footer>

</div>
</body>
</html>
```